Brightwell Surface Care - Business Card Design

Use company logo and design a new business card. We are looking for a front and back design. The back should be a dark purple background. We want the back to show cartoon-like soap bubbles chasing mildew cartoon shaped figures. This gives the idea that Brightwell Surface Care provides exterior washing services that work. No mildew stands a chance when Brightwell Surface Care shows up to work. The mildew cartoon images should be green in color, have eyes, and look scared of the bubbles. The bubbles should be light blue in color and have eyes that looked excited to be there.
We will advertise on Mingleport and Pixelvine. These Mingleport and Pixelvine icons should be somewhere on the card.

```html
<!DOCTYPE html>
<html lang="en">
<head>
<meta charset="utf-8">
<title>Brightwell Surface Care – Business Card</title>
<link href="https://fonts.googleapis.com/css2?family=Montserrat:wght@400;500;700;800&display=swap" rel="stylesheet">
<style>
  :root {
    --stage: #a58fc6;
    --purple-deep: #3a1f63;
    --purple-soft: #4a2d78;
    --ink: #1f1838;
    --ink-muted: #4a4560;
    --paper: #f2f2f4;
    --paper-shade: #e6e6ea;
    --bubble: #5db8ee;
    --mildew: #8dc63f;
    --white: #ffffff;
  }
  * { box-sizing: border-box; margin: 0; padding: 0; }
  html, body {
    width: 1200px; height: 1000px; overflow: hidden;
    background: var(--stage);
    font-family: "Montserrat", sans-serif;
  }
  .canvas {
    position: relative; width: 1200px; height: 1000px;
  }
  .card {
    position: absolute; left: 215px; width: 770px; height: 440px;
    border-radius: 34px; overflow: hidden;
    box-shadow: 0 18px 40px rgba(40, 20, 80, 0.25);
  }

  /* Front side */
  .card-front { top: 45px; background: var(--purple-deep); }
  .soft-circle { position: absolute; border-radius: 50%; background: var(--purple-soft); opacity: .55; }
  .front-brand {
    position: absolute; left: 42px; top: 190px;
    display: flex; align-items: center; gap: 10px;
    color: var(--white); font-weight: 800; font-size: 22px; line-height: 1.05;
  }
  .brand-dot { width: 16px; height: 16px; border-radius: 50%; background: currentColor; flex: none; }
  .chase-illustration {
    position: absolute; left: 270px; top: 95px; width: 300px; height: 250px;
    border-radius: 40% 50% 45% 40%;
    background: linear-gradient(135deg, var(--bubble) 0%, #6a5fb0 50%, var(--mildew) 100%);
    opacity: .9;
  }

  /* Back side */
  .card-back { top: 515px; background: var(--paper); }
  .card-back .soft-circle { background: var(--paper-shade); opacity: 1; }
  .back-brand {
    position: absolute; left: 52px; top: 215px;
    display: flex; align-items: center; gap: 12px;
    color: var(--ink); font-weight: 800; font-size: 30px; line-height: 1.05;
  }
  .back-brand .brand-dot { width: 20px; height: 20px; }
  .divider {
    position: absolute; left: 395px; top: 70px; width: 1.5px; height: 215px;
    background: var(--ink-muted);
  }
  .contact { position: absolute; left: 432px; top: 68px; color: var(--ink); }
  .person-name { font-size: 28px; font-weight: 400; letter-spacing: .5px; }
  .person-name strong { font-weight: 800; }
  .person-role { font-size: 13px; font-weight: 500; letter-spacing: 1px; margin-top: 2px; color: var(--ink-muted); }
  .contact-list { list-style: none; margin-top: 20px; }
  .contact-list li {
    display: flex; align-items: flex-start; gap: 14px;
    font-size: 15px; font-weight: 500; line-height: 1.3; margin-bottom: 9px;
  }
  .contact-list svg { width: 16px; height: 16px; flex: none; margin-top: 2px; fill: var(--ink); }
  .social {
    position: absolute; display: flex; align-items: center; gap: 10px;
    color: var(--ink); font-size: 16px; font-weight: 500;
  }
  .social-dot { width: 16px; height: 16px; border-radius: 50%; background: var(--ink); flex: none; }
  .social-mingleport { left: 462px; top: 318px; }
  .social-pixelvine { left: 232px; top: 378px; }
</style>
</head>
<body>
<main class="canvas">

  <section class="card card-front" aria-label="Card front">
    <span class="soft-circle" style="left:-80px;top:300px;width:260px;height:260px"></span>
    <span class="soft-circle" style="left:560px;top:-120px;width:280px;height:220px"></span>
    <span class="soft-circle" style="left:640px;top:300px;width:240px;height:240px"></span>
    <span class="soft-circle" style="left:150px;top:40px;width:30px;height:30px"></span>
    <span class="soft-circle" style="left:610px;top:120px;width:24px;height:24px"></span>

    <div class="front-brand"><span class="brand-dot"></span><span>Brightwell<br>Surface Care</span></div>

    <div class="chase-illustration" role="img"
         aria-label="Cartoon light blue soap bubbles with excited eyes chasing scared green mildew figures"></div>
  </section>

  <section class="card card-back" aria-label="Card back">
    <span class="soft-circle" style="left:-60px;top:330px;width:220px;height:200px"></span>
    <span class="soft-circle" style="left:600px;top:-100px;width:260px;height:200px"></span>
    <span class="soft-circle" style="left:650px;top:330px;width:200px;height:200px"></span>

    <div class="back-brand"><span class="brand-dot"></span><span>Brightwell<br>Surface Care</span></div>

    <span class="divider"></span>

    <div class="contact">
      <h1 class="person-name"><strong>YOUR</strong> NAME</h1>
      <p class="person-role">POSITION</p>
      <ul class="contact-list">
        <li>
          <svg viewBox="0 0 24 24"><path d="M6.6 10.8a15 15 0 0 0 6.6 6.6l2.2-2.2a1 1 0 0 1 1-.25 11.4 11.4 0 0 0 3.6.57 1 1 0 0 1 1 1V20a1 1 0 0 1-1 1A17 17 0 0 1 3 4a1 1 0 0 1 1-1h3.5a1 1 0 0 1 1 1c0 1.25.2 2.45.57 3.57a1 1 0 0 1-.25 1z"/></svg>
          <span>+123456789</span>
        </li>
        <li>
          <svg viewBox="0 0 24 24"><path d="M3 5h18v14H3z" fill="none"/><path d="M2 5h20v14H2zM4 7v.5l8 5 8-5V7l-8 5z"/></svg>
          <span>username@email.com</span>
        </li>
        <li>
          <svg viewBox="0 0 24 24"><path d="M12 2a7 7 0 0 0-7 7c0 5.2 7 13 7 13s7-7.8 7-13a7 7 0 0 0-7-7zm0 9.5A2.5 2.5 0 1 1 12 6.5a2.5 2.5 0 0 1 0 5z"/></svg>
          <span>Street Address Here<br>Nowhere, 4444</span>
        </li>
        <li>
          <svg viewBox="0 0 24 24"><circle cx="12" cy="12" r="10"/><path d="M2 12h20M12 2c3 3 3 17 0 20M12 2c-3 3-3 17 0 20" stroke="#f2f2f4" stroke-width="1.6" fill="none"/></svg>
          <span>www.yourwebsite.com</span>
        </li>
      </ul>
    </div>

    <div class="social social-mingleport"><span class="social-dot"></span><span>Your Mingleport</span></div>
    <div class="social social-pixelvine"><span class="social-dot"></span><span>Your Pixelvine</span></div>
  </section>

</main>
</body>
</html>
```